Business Card Design for Property Investment Company

We need a new business card designed that reflects our new domain. and also reflects more closely the style and branding of our website www.kplventures.co.uk

The template will be the same for two different directors. Logo and images from website, as well as more detail on brief are attached

Want a two-side design
Details from above image need to change as follows:
E: marcus.ellwood@kplventures.co.uk
W: www.kplventures.co.uk

Also, need second card, same design, for:
Simon Ellwood
Director
M: +44 (0)7812 639174
E: simon.ellwood@kplventures.co.uk
A: same as above
W: same as above

Attached are a selection of images from the website that could be used on the website, as well as the logo

Target Market(s)

Property/Real-estate professionals, invesroea and developers

Industry/Entity Type

Real Estate Development

Contact Information for Business Card

see brief attachment

Font styles to use
Sans Serif

Requirements
Must have
• Contact info as per brief
• Look and feel of the website - www.kplventures.co.uk
• (a selection of images that can be used have been attached, along with logo)
• Slick and professional look
Nice to have
• maybe include an image on one side of the card with logo, and contact info on the other (only a suggestion)
Should not have
• anything gimmicky

```html
<!DOCTYPE html>
<html lang="en">
<head>
<meta charset="utf-8">
<title>kpl ventures business card</title>
<link rel="stylesheet" href="https://fonts.googleapis.com/css2?family=Poppins:wght@300;400;600&display=swap">
<style>
  :root {
    --brand-green: #0b5e48;
    --card-white: #f4f4f3;
    --card-shade: #e6e6e4;
    --ink-green: #0d5a45;
    --photo-wall: #a9c2bd;
    --photo-light: #cfdcd8;
    --photo-dark: #6f7f7a;
    --stage: #d9d6d0;
    --paper: #ffffff;
  }
  * { box-sizing: border-box; margin: 0; padding: 0; }
  html, body {
    width: 1200px; height: 780px; overflow: hidden;
    background: var(--stage);
    font-family: "Poppins", sans-serif;
  }
  .stage {
    position: relative; width: 1200px; height: 780px;
    display: flex; justify-content: center; align-items: center; gap: 80px;
  }
  .card {
    position: relative; width: 400px; height: 620px;
    border-radius: 30px; overflow: hidden;
    box-shadow: 0 10px 28px rgba(0,0,0,0.18);
  }

  /* front side */
  .card-front .photo-fill {
    position: absolute; inset: 0;
    background: linear-gradient(160deg, var(--photo-light) 0%, var(--photo-wall) 45%, var(--photo-dark) 100%);
  }
  .front-name {
    position: absolute; left: 40px; bottom: 44px;
    font-weight: 600; font-size: 30px; line-height: 1;
    color: var(--paper);
  }

  /* back side */
  .card-back {
    background: radial-gradient(circle at 60% 40%, #fbfbfa 0%, var(--card-white) 55%, var(--card-shade) 100%);
  }
  .back-mark {
    position: absolute; top: 70px; left: 44px;
    display: flex; align-items: center; gap: 14px;
  }
  .back-mark .dot {
    width: 34px; height: 34px; border-radius: 50%;
    background: var(--brand-green);
  }
  .brand-name {
    font-weight: 600; font-size: 30px; line-height: 1;
    color: var(--brand-green);
  }
  .contact {
    position: absolute; left: 44px; bottom: 52px; right: 30px;
    color: var(--ink-green);
  }
  .person-name { font-weight: 600; font-size: 30px; line-height: 1.1; }
  .person-role { font-weight: 300; font-size: 17px; margin-bottom: 26px; }
  .address { font-weight: 300; font-size: 17px; line-height: 1.35; margin-bottom: 20px; }
  .lines { list-style: none; font-weight: 300; font-size: 16px; line-height: 1.5; }
  .lines b { font-weight: 600; display: inline-block; width: 26px; }
</style>
</head>
<body>
<main class="stage">
  <section class="card card-front">
    <div class="photo-fill" role="img" aria-label="Photograph of a framed black and white street print hanging on a pale green wall above a desk"></div>
    <p class="front-name">kpl ventures</p>
  </section>

  <section class="card card-back">
    <div class="back-mark">
      <span class="dot"></span>
      <span class="brand-name">kpl ventures</span>
    </div>
    <div class="contact">
      <h1 class="person-name">Simon Ellwood</h1>
      <p class="person-role">Director</p>
      <p class="address">18 Harrow Lane<br>Bexley, Kent, DA5 2QT</p>
      <ul class="lines">
        <li><b>M:</b>+44 (0)7812 639174</li>
        <li><b>E:</b>simon.ellwood@kplventures.co.uk</li>
        <li><b>W:</b>www.kplventures.co.uk</li>
      </ul>
    </div>
  </section>
</main>
</body>
</html>
```